Flyer for Mountain Bike Skills Event

Create an 11x17 posts for an upcoming Mountain Bike Skills event.

Falcon Trail Riding Academy Logo
--
Are you ready to ride your mountain bike faster and with more confidence? Join us to learn how to take your riding to the next level!
--
EVENT INFORMATION:

Saturday April 23
>> Fundamental Skills Clinic
>> Jumping Mini Clinic

Sunday April 24
>> Intermediate / Advanced Skills Clinic

Saturday - Sunday April 23/24
>> 2 Day Skills Camp

--
San Diego, California
--
Following your clinic, you will see an immediate improvement in your riding and a boost in confidence.

Skills taught and practiced in courses include:

Mind skills
Mastering manual front-wheel lifts
Manual dropping roots & steps
Cornering with speed & confidence
Reading & breaking down the trail
Introduction to energy management & flow
Linking trail sections for flow
Attacking flat corners
Flat and cambered corners
Bermed corners; lines and pumping
Switchbacks
Maximizing grip and traction with pumping
Learning to pump for speed & air

Event hosted by: HARLOWE CYCLE DEPOT (*use logo)

Sign up today!
--
More informaiton on our website:
WWW.PEDALWITHPOISE.COM

Target Market(s)

Mountain bikers age 35-60

Industry/Entity Type

Fitness

Requirements
Must have
• Falcon Logo
• Should be consistent with the Falcon brand, see website for examples: https://coastaltrailcraftlessons.com/ and our truck wrap design file.
• Flyer needs to be easy to read and include all the content in the project description.
Nice to have
• Include our tag line: SOAR LIKE A FALCON

```html
<!DOCTYPE html>
<html lang="en">
<head>
<meta charset="utf-8">
<title>Falcon Trail Riding Academy – Skills Event Flyer</title>
<link rel="stylesheet" href="https://fonts.googleapis.com/css2?family=Libre+Baskerville:wght@400;700&family=Oswald:wght@300;400;500;700&family=Roboto:wght@300&display=swap">
<style>
  :root {
    --page-bg: #e8e5e0;
    --paper: #ffffff;
    --ink: #1e1e1e;
    --magenta: #e8205f;
    --rule: #2a2a2a;
    --shadow-band: #d4d4d4;
    --sky: #7fb6e6;
    --hill: #8c9a56;
    --grass: #c7a84a;
  }
  * { margin: 0; padding: 0; box-sizing: border-box; }
  html, body { width: 1200px; height: 1200px; overflow: hidden; background: var(--page-bg); }
  .flyer {
    position: absolute; left: 230px; top: 27px;
    width: 740px; height: 1145px;
    background: var(--paper);
    box-shadow: 0 6px 18px rgba(0,0,0,.25);
    font-family: "Libre Baskerville", Georgia, serif;
    color: var(--ink);
    overflow: hidden;
  }
  .abs { position: absolute; white-space: nowrap; line-height: 1; }
  .art { position: absolute; left: 0; top: 0; }

  .brand { left: 22px; top: 30px; display: flex; align-items: center; gap: 14px; }
  .brand-mark { width: 46px; height: 46px; border-radius: 50%; background: var(--magenta); flex: none; }
  .brand-name { font-family: "Oswald", Arial, sans-serif; font-weight: 700; font-size: 30px; line-height: 1.05; color: var(--ink); text-transform: uppercase; white-space: normal; width: 220px; }

  .intro { right: 14px; top: 16px; text-align: right; color: #fff; font-size: 16.5px; line-height: 26px; letter-spacing: -.2px; }
  .intro strong { font-weight: 700; }

  .event-title { left: 440px; top: 150px; font-size: 19px; letter-spacing: 1px; }
  .day { font-size: 18px; }
  .session { font-size: 14.5px; font-weight: 700; letter-spacing: .4px; }
  .session::before { content: "•"; margin-right: 22px; }
  .session.wrap::before { margin-right: 24px; }
  .cont { font-size: 14.5px; font-weight: 700; letter-spacing: .4px; }

  .location { left: 515px; top: 462px; font-family: "Oswald", Arial, sans-serif; font-weight: 300; font-size: 30px; color: #fff; letter-spacing: -.5px; transform: scaleX(.9); transform-origin: left; }

  .promise { left: 508px; top: 515px; width: 220px; text-align: center; white-space: normal; font-size: 11px; font-weight: 700; line-height: 17px; }
  .skills-head { left: 508px; top: 578px; width: 220px; text-align: center; white-space: normal; font-size: 14px; line-height: 20.5px; color: var(--magenta); }

  .skills { position: absolute; left: 0; top: 0; list-style: none; font-family: "Roboto", Arial, sans-serif; font-weight: 300; font-size: 14px; color: var(--ink); }
  .skills li { position: absolute; white-space: nowrap; line-height: 1; letter-spacing: -.3px; }
  .skills li::before { content: "• "; }

  .host-label { left: 19px; top: 1015px; font-family: "Oswald", Arial, sans-serif; font-weight: 400; font-size: 11.5px; }
  .host { left: 22px; top: 1036px; display: flex; flex-direction: column; align-items: flex-start; gap: 8px; width: 100px; }
  .host-mark { width: 40px; height: 40px; border-radius: 50%; background: var(--ink); flex: none; }
  .host-name { font-family: "Oswald", Arial, sans-serif; font-weight: 500; font-size: 12px; line-height: 1.2; color: var(--ink); white-space: normal; width: 100px; }

  .signup { left: 139px; top: 1063px; font-family: "Oswald", Arial, sans-serif; font-weight: 300; font-size: 23px; }
  .more-info { left: 523px; top: 1038px; transform: translateX(-50%); font-family: "Oswald", Arial, sans-serif; font-weight: 300; font-size: 28px; }
  .url { left: 523px; top: 1082px; transform: translateX(-50%); font-family: "Oswald", Arial, sans-serif; font-weight: 700; font-size: 29px; }
</style>
</head>
<body>
<main class="flyer">
  <svg class="art" width="740" height="1145" viewBox="0 0 740 1145">
    <defs>
      <linearGradient id="trail-photo" x1="0" y1="0" x2="0" y2="1">
        <stop offset="0" stop-color="var(--sky)"/>
        <stop offset=".16" stop-color="#a9c6de"/>
        <stop offset=".3" stop-color="var(--hill)"/>
        <stop offset=".65" stop-color="#9aa35a"/>
        <stop offset="1" stop-color="var(--grass)"/>
      </linearGradient>
    </defs>
    <polygon class="header-band" points="358,0 740,0 740,122 304,122" fill="var(--magenta)"/>
    <polygon class="photo-edge" points="0,122 384,122 508,482 417,1004 0,1004" fill="var(--shadow-band)"/>
    <polygon points="0,122 378,122 502,482 411,1004 0,1004" fill="url(#trail-photo)" role="img" aria-label="Photo of a mountain biker in full-face helmet leaning hard into a dusty corner on a grassy hillside trail"/>
    <polygon class="location-band" points="500,458 740,458 740,500 503,500 510,479" fill="var(--magenta)"/>
    <rect class="footer-rule" x="0" y="1003" width="740" height="2.5" fill="var(--rule)"/>
  </svg>

  <div class="abs brand">
    <span class="brand-mark"></span>
    <span class="brand-name">Falcon Trail Riding Academy</span>
  </div>

  <p class="abs intro">Are you ready to ride your <strong>MOUNTAIN</strong><br><strong>BIKE FASTER</strong> and <strong>WITH MORE</strong><br><strong>CONFIDENCE?</strong> Join us to learn how to<br>take your riding to the next level!</p>

  <h2 class="abs event-title">EVENT INFORMATION</h2>
  <p class="abs day" style="left:420px;top:178px">Saturday April 23</p>
  <p class="abs session" style="left:440px;top:213px">Fundamental Skills Clinic</p>
  <p class="abs session" style="left:462px;top:243px">Jumping Mini Clinic</p>
  <p class="abs day" style="left:455px;top:273px">Sunday April 24</p>
  <p class="abs session wrap" style="left:496px;top:309px">Intermediate / Advanced</p>
  <p class="abs cont" style="left:522px;top:330px">Skills Clinic</p>
  <p class="abs day" style="left:487px;top:360px">Saturday - Sunday</p>
  <p class="abs day" style="left:544px;top:385px">April 23/24</p>
  <p class="abs session" style="left:530px;top:420px">2 Day Skills Camp</p>

  <p class="abs location">San Diego, California</p>

  <p class="abs promise">Following your clinic, you will see an immediate improvement in your riding and a boost in confidence.</p>
  <p class="abs skills-head">Skills taught and practiced in courses include:</p>

  <ul class="skills">
    <li style="left:494px;top:626px">Mind skills</li>
    <li style="left:490px;top:653px">Mastering manual front-wheel lifts</li>
    <li style="left:487px;top:681px">Manual dropping roots &amp; steps</li>
    <li style="left:480px;top:708px">Cornering with speed &amp; confidence</li>
    <li style="left:475px;top:736px">Reading &amp; breaking down the trail</li>
    <li style="left:470px;top:763px;line-height:23px">Introduction to energy management &amp;<br>&nbsp;flow</li>
    <li style="left:462px;top:814px">Linking trail sections for flow</li>
    <li style="left:457px;top:842px">Attacking flat corners</li>
    <li style="left:452px;top:869px">Flat and cambered corners</li>
    <li style="left:448px;top:897px">Bermed corners; lines and pumping</li>
    <li style="left:443px;top:924px">Switchbacks</li>
    <li style="left:438px;top:953px">Maximizing grip and traction with pumping</li>
    <li style="left:434px;top:980px">Learning to pump for speed &amp; air</li>
  </ul>

  <p class="abs host-label">Event hosted by:</p>
  <div class="abs host">
    <span class="host-mark"></span>
    <span class="host-name">HARLOWE CYCLE DEPOT</span>
  </div>
  <p class="abs signup">Sign up today!</p>
  <p class="abs more-info">More informaiton on our website</p>
  <p class="abs url">WWW.PEDALWITHPOISE.COM</p>
</main>
</body>
</html>
```